Etiketten für Brennerei aus Tirol
Zielgruppe
Wir sind eine Brennerei aus Tirol bzw. Südtirol, produzieren in Österreich hochwertige Obstbrände und beliefern mit unseren Bränden, Schnäpsen und Spirituosen den Lebensmittel Einzelhandel (kein Discount) in Österreich und Deutschland. Zielkunden sind Genießer, die die österreichische bzw. Südtiroler Gastlichkeit und Lebenskultur schätzen.
Für eine neue Produktlinie mit Gin / Whisky und Wodka möchten wir ein ganz neues Etikettendesign umsetzen.
Aufgabenstellung
Beiliegend Abbildung der Flasche und Skizze.
Wir möchten Tiroler Werte vemritteln -
Ehrlich kantig authentisch , naturverbunden, autonom
Tiroler Symbole können eingesetzt werden.
Stichworte: Manufaktur, Handcrafted
Bezeichnungen: Handcrafted Dry Gin, Premium Whiskey, Premium Wodka
Technik:
Rundumetikett oder
Ätzdruck auf Flasche

```html
<!DOCTYPE html>
<html lang="de">
<head>
<meta charset="utf-8">
<title>Gipfelhaus Alpenkost – Etiketten Whiskey, Dry Gin, Wodka</title>
<link rel="stylesheet" href="https://fonts.googleapis.com/css2?family=Uncial+Antiqua&family=Oswald:wght@400;500&family=Dancing+Script:wght@500&display=swap">
<style>
  :root {
    --page: #ffffff;
    --whiskey-top: #7e2410;
    --whiskey-mid: #b4481a;
    --whiskey-low: #d9883c;
    --whiskey-ink: #efe3c4;
    --whiskey-mountain: #e3a86c;
    --clear-glass: #e7eaed;
    --clear-glass-edge: #dadee2;
    --gin-ink: #a87572;
    --gin-mountain: #c39a94;
    --wodka-ink: #8b90c9;
    --wodka-mountain: #a2a6d6;
  }
  * { box-sizing: border-box; margin: 0; padding: 0; }
  html, body { width: 1200px; height: 612px; overflow: hidden; background: var(--page); }
  .canvas { position: relative; width: 1200px; height: 612px; }

  .label {
    position: absolute; top: 190px; width: 164px; height: 262px;
    border-radius: 8px 8px 4px 4px; overflow: hidden;
  }
  .label > * { position: absolute; left: 0; right: 0; text-align: center; }
  .label--whiskey { left: 70px; color: var(--whiskey-ink);
    background: linear-gradient(180deg, var(--whiskey-top) 0%, var(--whiskey-mid) 50%, var(--whiskey-low) 100%); }
  .label--gin { left: 525px; color: var(--gin-ink);
    background: linear-gradient(180deg, var(--clear-glass) 0%, var(--clear-glass-edge) 100%); }
  .label--wodka { left: 952px; color: var(--wodka-ink);
    background: linear-gradient(180deg, var(--clear-glass) 0%, var(--clear-glass-edge) 100%); }

  .brand { top: 56px; font-family: "Oswald", sans-serif; line-height: 1; }
  .brand__name { display: block; font-size: 12px; font-weight: 500; letter-spacing: .4px; }
  .brand__line { display: block; font-size: 7px; font-weight: 400; letter-spacing: 1.3px; margin-top: 3px; }

  .rule-title {
    top: 92px; left: 18px; right: 18px;
    display: flex; align-items: center; gap: 5px;
    font-family: "Uncial Antiqua", serif; font-size: 9px; line-height: 1;
  }
  .rule-title::before, .rule-title::after { content: ""; flex: 1; border-top: 1px dashed currentColor; }
  .rule { left: 18px; right: 18px; height: 0; border-top: 1px dashed currentColor; }

  .product { font-family: "Uncial Antiqua", serif; font-weight: 400; line-height: 1; }
  .product--whiskey { top: 104px; font-size: 27px; }
  .product--wodka { top: 104px; font-size: 31px; }
  .product--gin { top: 104px; font-size: 48px; }
  .product__small { position: absolute; top: 96px; left: 44px; right: 0; font-family: "Uncial Antiqua", serif; font-size: 22px; line-height: 1; }

  .script { font-family: "Dancing Script", cursive; font-size: 10px; line-height: 1; text-align: right; padding-right: 22px; }

  .seal {
    width: 40px; height: 40px; right: auto;
    border-radius: 50%; border: 2px solid currentColor; z-index: 2;
  }
  .label--whiskey .seal { background: var(--whiskey-ink); border-color: var(--whiskey-top); }

  .mountains { top: auto; bottom: 0; height: 86px; }
  .label--whiskey .mountains { background: linear-gradient(180deg, rgba(180,72,26,0) 0%, var(--whiskey-mountain) 100%); }
  .label--gin .mountains { background: linear-gradient(180deg, rgba(231,234,237,0) 0%, var(--gin-mountain) 100%); }
  .label--wodka .mountains { background: linear-gradient(180deg, rgba(231,234,237,0) 0%, var(--wodka-mountain) 100%); }
</style>
</head>
<body>
<main class="canvas">

  <section class="label label--whiskey" aria-label="Etikett Premium Whiskey">
    <p class="brand"><span class="brand__name">GIPFELHAUS</span><span class="brand__line">ALPENKOST</span></p>
    <p class="rule-title">Premium</p>
    <h2 class="product product--whiskey">Whiskey</h2>
    <span class="rule" style="top:148px"></span>
    <p class="script" style="top:154px">handcrafted</p>
    <span class="seal" style="left:16px;top:160px" aria-hidden="true"></span>
    <div class="mountains" role="img" aria-label="Gravierte Felsgipfel-Landschaft"></div>
  </section>

  <section class="label label--gin" aria-label="Etikett Handcrafted Dry Gin">
    <p class="brand"><span class="brand__name">GIPFELHAUS</span><span class="brand__line">ALPENKOST</span></p>
    <p class="script" style="top:86px;text-align:center;padding:0 30px 0 0">handcrafted</p>
    <span class="rule" style="top:100px"></span>
    <p class="product__small">Dry</p>
    <h2 class="product product--gin" style="top:118px">Gin</h2>
    <span class="rule" style="top:172px"></span>
    <span class="seal" style="left:9px;top:167px" aria-hidden="true"></span>
    <div class="mountains" role="img" aria-label="Gravierte Felsgipfel-Landschaft"></div>
  </section>

  <section class="label label--wodka" aria-label="Etikett Premium Wodka">
    <p class="brand"><span class="brand__name">GIPFELHAUS</span><span class="brand__line">ALPENKOST</span></p>
    <p class="rule-title">Premium</p>
    <h2 class="product product--wodka">Wodka</h2>
    <span class="rule" style="top:154px"></span>
    <p class="script" style="top:164px">handcrafted</p>
    <span class="seal" style="left:7px;top:159px" aria-hidden="true"></span>
    <div class="mountains" role="img" aria-label="Gravierte Felsgipfel-Landschaft"></div>
  </section>

</main>
</body>
</html>
```